Business Carss for Harborlight Church

Need a progressive looking/modern business card design for my church

Target Market(s)

Families and young adults

Industry/Entity Type

Religious

Contact Information for Business Card

4728 Willow Crest Rd.
Frankfort Ky
502-318-4472

Rev. Tommy Fenwick
Slogan: Honor God and Make Discies

Font styles to use
Serif
Sans Serif
Decorative
Script

Colors
0555a3
3176b5

Requirements
Should not have
• Should not have a template look
• A unique out of the box look

```html
<!DOCTYPE html>
<html lang="en">
<head>
<meta charset="utf-8">
<title>Harborlight Church – Business Card</title>
<link rel="stylesheet" href="https://fonts.googleapis.com/css2?family=Nunito+Sans:wght@400;600;700;800&display=swap">
<style>
  :root {
    --backdrop: #b4b4b4;
    --paper: #ececec;
    --navy: #2f3963;
    --ink: #161616;
    --white: #f4f4f4;
  }
  * { margin: 0; padding: 0; box-sizing: border-box; }
  html, body {
    width: 1200px;
    height: 1000px;
    overflow: hidden;
    background: var(--backdrop);
    font-family: "Nunito Sans", sans-serif;
  }
  .canvas {
    position: relative;
    width: 1200px;
    height: 1000px;
  }
  .card {
    position: absolute;
    left: 220px;
    width: 760px;
    height: 421px;
    overflow: hidden;
    box-shadow: 0 2px 6px rgba(0,0,0,0.18);
  }
  .card--front { top: 56px; background: var(--paper); }
  .card--back { top: 523px; background: var(--navy); color: var(--white); }

  .front-arrow {
    position: absolute;
    inset: 0;
    width: 100%;
    height: 100%;
  }
  .wordmark {
    font-weight: 800;
    font-size: 40px;
    line-height: 1;
    letter-spacing: 0.5px;
    white-space: nowrap;
  }
  .card--front .wordmark {
    position: absolute;
    left: 64px;
    top: 116px;
    color: var(--ink);
  }
  .contact-name {
    position: absolute;
    left: 62px;
    top: 248px;
    font-weight: 800;
    font-size: 27px;
    color: var(--navy);
  }
  .contact-role {
    position: absolute;
    left: 63px;
    top: 286px;
    font-size: 19px;
    color: var(--ink);
  }
  .contact-rule {
    position: absolute;
    left: 63px;
    top: 326px;
    width: 48px;
    height: 1px;
    background: #777;
  }
  .contact-address {
    position: absolute;
    left: 63px;
    top: 350px;
    font-size: 19px;
    color: var(--ink);
  }

  .card--back .wordmark {
    position: absolute;
    left: 0;
    right: 0;
    top: 160px;
    text-align: center;
    font-size: 44px;
  }
  .welcome-line {
    position: absolute;
    left: 0;
    right: 0;
    top: 226px;
    text-align: center;
    font-size: 18px;
    font-weight: 400;
    letter-spacing: 0.5px;
  }
  .service-times {
    position: absolute;
    left: 0;
    right: 0;
    top: 348px;
    text-align: center;
    font-size: 19px;
    letter-spacing: 3px;
  }
</style>
</head>
<body>
<main class="canvas">

  <section class="card card--front" aria-label="Business card front">
    <svg class="front-arrow" viewBox="0 0 655 363" preserveAspectRatio="none">
      <polygon fill="#2f3963" points="414,363 487,363 578,162 602,170 587,60 480,128 515,140"/>
      <text x="0" y="0" transform="translate(503 244) rotate(-65.6)" text-anchor="middle" dominant-baseline="middle"
            fill="#f4f4f4" font-family="Nunito Sans, sans-serif" font-weight="800" font-size="19">502-318-4472</text>
    </svg>
    <div class="wordmark">Harborlight Church</div>
    <div class="contact-name">Rev. Tommy Fenwick</div>
    <div class="contact-role">Lead Pastor</div>
    <div class="contact-rule"></div>
    <div class="contact-address">4728 Willow Crest Rd., Frankfort Ky</div>
  </section>

  <section class="card card--back" aria-label="Business card back">
    <div class="wordmark">Harborlight Church</div>
    <div class="welcome-line">A place to belong</div>
    <div class="service-times">Service Times 10:30 A.M.</div>
  </section>

</main>
</body>
</html>
```